Beauty Therapy Web Design

I need a web page design for a small beauty therapy clinic, the owner is currently the only beauty therapist working there.
We require the following pages:
Home
About
Treatments
Nails
Courses
Contact
I will attach the clinics business card, treatment menu and signage so that you get a feeling for the branding colours etc.
This is the first website for the beauty therapist, she would like to attract new clients and also tourists that come in on the cruise ships. The thing that sets her apart from other clinics is that she welcomes texting for appointments.
I have selected refundable because I have never done this before so I don't know what to expect, I have the full intention of going through with it as long as I get a good design.
Feel free to ask for further information
Reason: Project extended as I am away for work and am unable to meet with the owner.
Target Market(s)
Females 18 to 50
Industry/Entity Type
Business
Look and feel
Each slider illustrates characteristics of the customer's brand and the style your logo design should communicate.

```html
<!DOCTYPE html>
<html lang="en">
<head>
<meta charset="utf-8">
<title>Lumera Beauty Therapy – Home</title>
<link rel="stylesheet" href="https://fonts.googleapis.com/css2?family=Dosis:wght@300;400;500;600&display=swap">
<style>
  :root {
    --brand-purple: #a64bb4;
    --brand-deep: #4b1566;
    --heading-purple: #8c1a90;
    --text-grey: #7a7a7a;
    --white: #ffffff;
    --panel-bg: rgba(255, 255, 255, 0.86);
    --hero-light: #fbe6ec;
    --hero-mid: #f1c3cf;
    --hero-skin: #e9c4b8;
  }
  * { margin: 0; padding: 0; box-sizing: border-box; }
  html, body { width: 1200px; height: 764px; overflow: hidden; background: var(--white); }
  body { font-family: "Dosis", sans-serif; position: relative; }

  .contact-bar {
    position: absolute; top: 4px; right: 117px; height: 22px;
    display: flex; gap: 30px; white-space: nowrap;
    color: var(--brand-deep); font-size: 15px; font-weight: 500; line-height: 20px;
  }

  .nav-band {
    position: absolute; top: 28px; left: 0; width: 1200px; height: 48px;
    background: var(--brand-purple);
  }
  .main-nav { position: absolute; top: 0; left: 0; width: 100%; height: 100%; }
  .main-nav a {
    position: absolute; top: 11px; color: var(--white); text-decoration: none;
    font-size: 20px; font-weight: 500; letter-spacing: 0.2px; white-space: nowrap;
  }
  .main-nav a.is-active { font-weight: 600; }
  .main-nav a.is-active::after {
    content: ""; position: absolute; left: -8px; right: -8px; top: 34px; height: 3px;
    background: var(--white);
  }

  .brand {
    position: absolute; top: 0; left: 127px; width: 309px; height: 94px;
    background: var(--white); z-index: 3; text-align: center;
  }
  .brand-name {
    display: block; margin-top: 10px; padding-left: 12px; font-size: 50px; line-height: 48px;
    font-weight: 500; color: var(--brand-deep); letter-spacing: 12px;
  }
  .brand-tagline {
    display: block; padding-left: 7px; font-size: 18px; font-weight: 500; color: var(--brand-deep);
    letter-spacing: 7px; margin-top: 3px; white-space: nowrap;
  }

  .hero {
    position: absolute; top: 76px; left: 0; width: 1200px; height: 688px;
    background:
      radial-gradient(ellipse 260px 300px at 90px 180px, #e98fb4 0%, rgba(233,143,180,0) 100%),
      radial-gradient(ellipse 420px 520px at 500px 300px, var(--hero-skin) 0%, rgba(233,196,184,0) 100%),
      linear-gradient(180deg, var(--hero-light) 0%, var(--hero-mid) 100%);
  }

  .welcome-panel {
    position: absolute; top: 317px; left: 505px; width: 600px; height: 360px;
    background: var(--panel-bg);
  }
  .welcome-title {
    position: absolute; top: 16px; left: 0; width: 100%; text-align: center;
    font-size: 47px; font-weight: 300; color: var(--heading-purple); letter-spacing: 0.5px;
    white-space: nowrap;
  }
  .welcome-title strong { font-weight: 400; }
  .welcome-text {
    position: absolute; top: 77px; left: 20px; width: 540px;
    font-size: 13px; line-height: 21.8px; color: var(--text-grey); font-weight: 500;
  }
  .welcome-text .lead { text-indent: 40px; }

  .feature {
    position: absolute; top: 235px; text-align: center; text-decoration: none;
  }
  .feature-photo { height: 93px; }
  .feature-label {
    margin-top: 3px; font-size: 15px; font-weight: 500; color: var(--heading-purple);
    white-space: nowrap;
  }
  .feature-facial { left: 20px; width: 171px; }
  .feature-facial .feature-photo { background: linear-gradient(135deg, #f4e3dc, #e6c6b6); }
  .feature-body { left: 215px; width: 167px; }
  .feature-body .feature-photo { background: linear-gradient(135deg, #c98a5c, #6b3f25); }
  .feature-gallery { left: 403px; width: 176px; }
  .feature-gallery .feature-photo { background: linear-gradient(135deg, #5a4660, #d9cfd6); }
</style>
</head>
<body>
  <div class="hero" role="img" aria-label="Close-up beauty photograph of a woman with a pink orchid beside her face"></div>

  <header>
    <div class="contact-bar">
      <span class="contact-email">E: info@lumera-beauty.com</span>
      <span class="contact-phone">T: 00 5550-0142</span>
    </div>
    <div class="nav-band">
      <nav class="main-nav">
        <a href="#" class="is-active" style="left:542px">HOME</a>
        <a href="#" style="left:613px">ABOUT</a>
        <a href="#" style="left:691px">TREATMENTS</a>
        <a href="#" style="left:822px">NAILS</a>
        <a href="#" style="left:897px">COURSES</a>
        <a href="#" style="left:998px">CONTACTS</a>
      </nav>
    </div>
    <div class="brand">
      <span class="brand-name">LUMERA</span>
      <span class="brand-tagline">BEAUTY THERAPY</span>
    </div>
  </header>

  <main class="welcome-panel">
    <h1 class="welcome-title">WELCOME TO <strong>LUMERA</strong></h1>
    <div class="welcome-text">
      <p class="lead">Lorem ipsum dolor sit amet, consectetur adipiscing elit. Maecenas blandit nunc ornare nibh tincidunt blandit. Sed hendrerit laoreet felis, sit amet sodales ligula bibendum sit amet. Duis porttitor molestie cursus.</p>
      <p>Aenean at magna feugiat dolor dapibus rhoncus quis sed leo. Etiam lacus nibh, tincidunt non consectetur sit amet, tristique ut justo. Integer in lorem malesuada quam euismod mattis. In hac habitasse platea dictumst. Sed dictum euismod mauris eu pulvinar.</p>
    </div>

    <a class="feature feature-facial" href="#">
      <div class="feature-photo" role="img" aria-label="Photo of a woman with smooth skin touching her face"></div>
      <div class="feature-label">FACIAL CONTOURING</div>
    </a>
    <a class="feature feature-body" href="#">
      <div class="feature-photo" role="img" aria-label="Photo of a relaxing back massage"></div>
      <div class="feature-label">BODY CONTOURING</div>
    </a>
    <a class="feature feature-gallery" href="#">
      <div class="feature-photo" role="img" aria-label="Photo of a facial mask treatment with steam"></div>
      <div class="feature-label">PHOTO GALLERY</div>
    </a>
  </main>
</body>
</html>
```